Loom Harbor commercial brochure

We need a brochure that presents our services for commercial use. Without going into the details of our offers, that the prospect understands our added value and our expertise for the creation of a showcase site, e-commerce site and personalized, tailor-made application.

Please respect the graphic charter

Target Market(s)

Small and medium enterprises

Colors
F0912C
F2A743
F7CA91
FBE8D2
FDF5EE

Requirements
Must have
• a good presentation of our offers on several different pages
Nice to have
• little text but a lot of clarity and precision in the information
Should not have
• too much information, heavy design

```html
<!DOCTYPE html>
<html lang="fr">
<head>
<meta charset="utf-8">
<title>Loom Harbor – Brochure commerciale</title>
<link rel="stylesheet" href="https://fonts.googleapis.com/css2?family=Comfortaa:wght@400;500;600;700&family=Montserrat:wght@400;500&display=swap">
<style>
  :root {
    --accent: #f4470f;
    --accent-soft: #f6b59c;
    --accent-pale: #fbd9cc;
    --ink: #1f1f24;
    --text: #3a3a40;
    --muted: #8a8a90;
    --paper: #ffffff;
    --paper-grey: #f4f4f4;
    --backdrop: #ebebeb;
    --rule: #d4d4d8;
  }
  * { box-sizing: border-box; margin: 0; padding: 0; }
  html, body { width: 1200px; height: 3200px; overflow: hidden; }
  body {
    background: var(--backdrop);
    position: relative;
    font-family: "Montserrat", Arial, sans-serif;
    color: var(--text);
  }
  .page {
    position: absolute;
    width: 512px;
    height: 660px;
    background: var(--paper);
    box-shadow: 0 3px 8px rgba(0,0,0,.12);
    overflow: hidden;
  }
  .cover { left: 344px; top: 480px; }
  .spread-vision { left: 58px; top: 1223px; width: 510px; }
  .spread-process { left: 632px; top: 1223px; width: 510px; }
  .back { left: 344px; top: 1968px; }

  .brand {
    position: absolute;
    display: flex;
    align-items: center;
    gap: 8px;
    font-family: "Comfortaa", Arial, sans-serif;
    font-weight: 700;
    color: var(--accent);
  }
  .brand-mark { width: 14px; height: 14px; background: var(--accent); }

  /* Cover */
  .cover .brand { left: 28px; top: 80px; font-size: 22px; }
  .corner-fold {
    position: absolute; right: 0; top: 0; width: 124px; height: 115px;
    background: linear-gradient(135deg, var(--accent-soft), var(--accent));
    clip-path: polygon(0 100%, 30% 0, 100% 0, 100% 75%);
  }
  .cover-title {
    position: absolute; left: 28px; top: 232px;
    font-family: "Comfortaa", Arial, sans-serif;
    font-weight: 600; font-size: 34px; line-height: 46px;
    color: var(--ink); text-transform: uppercase; letter-spacing: .5px;
  }
  .cover-title .lead { color: var(--accent); font-size: 43px; font-weight: 500; line-height: 50px; display: block; }
  .cover-title .tail { color: var(--accent); }
  .pattern-band {
    position: absolute; left: 0; right: 0; bottom: 0; height: 203px;
    background: linear-gradient(180deg, rgba(246,181,156,0) 0%, var(--accent-soft) 45%, var(--accent-soft) 100%);
    opacity: .85;
  }

  /* Spread sections */
  .panel { position: absolute; left: 0; right: 0; }
  .panel-top { top: 0; height: 326px; background: var(--paper); }
  .panel-bottom { top: 326px; bottom: 0; background: var(--paper); border-top: 1px solid #ececec; }
  .panel-bottom.grey { background: var(--paper-grey); }
  .spread-vision::after {
    content: ""; position: absolute; right: 0; top: 0; bottom: 0; width: 22px; background: var(--paper-grey);
  }

  .section-title {
    position: absolute;
    font-family: "Comfortaa", Arial, sans-serif;
    font-size: 17px; line-height: 20px; font-weight: 500; color: var(--ink);
  }
  .section-title .hl { color: var(--accent); display: block; }
  .section-title.big .hl { font-size: 25px; line-height: 30px; font-weight: 600; }
  .section-title.big { font-size: 16px; line-height: 24px; }

  .body-copy { position: absolute; font-size: 7.6px; line-height: 9.6px; color: var(--text); }
  .body-copy p + p { margin-top: 7px; }

  .illustration {
    position: absolute; border-radius: 6px;
    background: linear-gradient(160deg, #fde3d8 0%, #f6b59c 55%, #f4470f 100%);
    opacity: .55;
  }

  /* Back */
  .back .pattern-top {
    position: absolute; left: 0; top: 0; width: 430px; height: 242px;
    background: linear-gradient(110deg, var(--accent-pale) 0%, rgba(251,217,204,.6) 55%, rgba(251,217,204,0) 100%);
  }
  .back .pattern-corner {
    position: absolute; right: 0; bottom: 0; width: 60px; height: 100px;
    background: linear-gradient(200deg, rgba(246,181,156,0), var(--accent-soft));
  }
  .back .brand { left: 42px; top: 532px; font-size: 19px; }
  .back .divider { position: absolute; left: 201px; top: 478px; width: 1px; height: 136px; background: var(--rule); }
  .contact-list { position: absolute; left: 252px; top: 484px; list-style: none; }
  .contact-list li {
    display: flex; align-items: center; gap: 12px; height: 35px;
    font-size: 9.5px; color: var(--ink); font-weight: 500;
  }
  .contact-list svg { width: 24px; height: 24px; flex: none; }
</style>
</head>
<body>

  <!-- Cover -->
  <section class="page cover">
    <div class="brand"><span class="brand-mark"></span>Loom Harbor</div>
    <div class="corner-fold" role="img" aria-label="Formes géométriques décoratives en angle"></div>
    <h1 class="cover-title">
      <span class="lead">Agence digitale,</span>
      Spécialiste du web et<br>
      des applications<br>
      <span class="tail">mobiles</span>
    </h1>
    <div class="pattern-band" role="img" aria-label="Motif décoratif de triangles pêche"></div>
  </section>

  <!-- Spread: vision + restaurant app -->
  <section class="page spread-vision">
    <div class="panel panel-top">
      <h2 class="section-title" style="left:38px;top:29px;"><span class="hl">Notre Vision de</span>l’agence digitale</h2>
      <div class="body-copy" style="left:38px;top:86px;width:200px;">
        <p>Notre agence digitale met vos projets au cœur de chaque décision et vous aide à atteindre vos objectifs ensemble.</p>
        <p>Site web, application mobile ou campagne digitale : chaque projet est un défi que nous relevons avec réactivité, innovation et un conseil personnalisé.</p>
        <p>De la maquette à la création graphique, de l’UX design au référencement, nos professionnels vous accompagnent de A à Z.</p>
        <p>Notre vision du digital repose sur des solutions web et mobiles adaptées à vos besoins.</p>
      </div>
      <div class="illustration" style="left:268px;top:106px;width:204px;height:186px;" role="img" aria-label="Illustration d’une équipe en réunion autour d’une table"></div>
    </div>
    <div class="panel panel-bottom">
      <div class="illustration" style="left:0;top:84px;width:235px;height:250px;border-radius:0 6px 0 0;" role="img" aria-label="Illustration de mains tenant un smartphone avec une application de livraison"></div>
      <h2 class="section-title big" style="left:260px;top:50px;"><span class="hl">Nouveau :</span>L’application mobile<br>pour votre restaurant !</h2>
      <div class="body-copy" style="left:260px;top:152px;width:205px;">
        <p>Vous souhaitez booster votre chiffre d’affaires et gagner en réactivité auprès de vos clients ?</p>
        <p>Découvrez notre solution d’application mobile iOS et Android pour votre restaurant !</p>
        <p>Notre agence développe une application clés en main, au design dynamique, pour une expérience client optimale.</p>
        <p>Découvrez les avantages d’une application sur mesure, sans engagement et sans frais ! N’hésitez pas à nous contacter !</p>
      </div>
    </div>
  </section>

  <!-- Spread: process -->
  <section class="page spread-process">
    <div class="panel panel-top">
      <h2 class="section-title" style="left:41px;top:29px;"><span class="hl">Notre processus</span>application mobile</h2>
      <div class="body-copy" style="left:41px;top:76px;width:205px;">
        <p>La création de votre site web commence par l’expression d’un besoin : site vitrine, e-commerce ou sur-mesure.</p>
        <p>Une première phase de définition de la charte graphique et de maquettage est essentielle.</p>
        <p>Nos experts en web design proposent l’interface adaptée, nos développeurs utilisent les outils les plus performants.</p>
        <p>Nos rédacteurs SEO assurent à votre site une visibilité accrue et un conseil en marketing digital.</p>
        <p>Votre site web est votre vitrine. Nous le rendons attractif et performant !</p>
      </div>
      <div class="illustration" style="left:283px;top:77px;width:210px;height:190px;" role="img" aria-label="Illustration d’un développeur travaillant à son bureau"></div>
    </div>
    <div class="panel panel-bottom grey">
      <div class="illustration" style="left:9px;top:46px;width:205px;height:218px;" role="img" aria-label="Illustration d’une personne organisant des écrans d’application"></div>
      <h2 class="section-title" style="left:238px;top:20px;"><span class="hl">Notre processus</span>application mobile</h2>
      <div class="body-copy" style="left:238px;top:68px;width:235px;">
        <p>Développer une application mobile n’a jamais été aussi important pour votre stratégie web !</p>
        <p>Notre agence propose plusieurs possibilités pour une application compatible iOS et Android.</p>
        <p>Une application développée par Loom Harbor est un outil innovant, de qualité, avec une expérience utilisateur optimale.</p>
        <p>Nos applications sont livrées clés en main pour exploiter tout leur potentiel.</p>
        <p>Vous avez une boutique, un commerce ou un restaurant ?</p>
        <p>Notre solution d’application mobile dédiée est sans engagement et sans frais.</p>
        <p>Découvrez les avantages d’une solution sur-mesure et personnalisée !</p>
      </div>
    </div>
  </section>

  <!-- Back cover -->
  <section class="page back">
    <div class="pattern-top" role="img" aria-label="Motif décoratif de triangles rose pâle"></div>
    <div class="pattern-corner" role="img" aria-label="Petit motif décoratif de triangles"></div>
    <div class="brand"><span class="brand-mark"></span>Loom Harbor</div>
    <div class="divider"></div>
    <ul class="contact-list">
      <li>
        <svg viewBox="0 0 24 24" fill="none" stroke="#1f1f24" stroke-width="1.1"><circle cx="12" cy="12" r="11"/><path d="M8.5 7.5l2 0 1 2.5-1.3 1a6 6 0 0 0 2.8 2.8l1-1.3 2.5 1v2a1 1 0 0 1-1 1A8.5 8.5 0 0 1 7.5 8.5a1 1 0 0 1 1-1z"/></svg>
        01.42.58.36.90 / 04.91.27.63.15
      </li>
      <li>
        <svg viewBox="0 0 24 24" fill="none" stroke="#1f1f24" stroke-width="1.1"><circle cx="12" cy="12" r="11"/><rect x="6.5" y="8" width="11" height="8"/><path d="M6.5 8l5.5 4.5 5.5-4.5"/></svg>
        hello@loomharbor.com
      </li>
      <li>
        <svg viewBox="0 0 24 24" fill="none" stroke="#1f1f24" stroke-width="1.1"><circle cx="12" cy="12" r="11"/><circle cx="12" cy="12" r="6"/><path d="M6 12h12M12 6c-2.2 2.5-2.2 9.5 0 12M12 6c2.2 2.5 2.2 9.5 0 12"/></svg>
        loomharbor.studio
      </li>
      <li>
        <svg viewBox="0 0 24 24" fill="none" stroke="#1f1f24" stroke-width="1.1"><circle cx="12" cy="12" r="11"/><path d="M12 18s-4.5-4.5-4.5-7.5a4.5 4.5 0 0 1 9 0C16.5 13.5 12 18 12 18z"/><circle cx="12" cy="10.5" r="1.6"/></svg>
        contact@loomharbor.studio
      </li>
    </ul>
  </section>

</body>
</html>
```